Update patient consent forms and contract

Objective
Redesign the existing patient contract information document to create a modern,contempory, and easy-to-understand experience for patients. The updated design should improve readability, accessibility, and overall presentation while maintaining compliance with healthcare and legal requirements.

Key Deliverables

Refreshed visual design and layout
Improved information hierarchy and readability
Modern typography and colour palette aligned with brand guidelines
Clear section headings and navigation
Print-ready and digital versions (PDF)

Include KVE Logo within patient KVE consent to treatment. Ideally this document should be portrait not landscape.
Updates

I would love a front page to be included in the document

```html
<!DOCTYPE html>
<html lang="en">
<head>
<meta charset="utf-8">
<title>Patient Consent to Treatment</title>
<link href="https://fonts.googleapis.com/css2?family=Montserrat:wght@500;600;700&family=Questrial&display=swap" rel="stylesheet">
<style>
:root{
  --backdrop:#a5a69f;
  --band:#777970;
  --navy:#1b2a4e;
  --ink:#222426;
  --paper:#ffffff;
  --footer:#dcdcdc;
  --tick:#77796f;
}
*{box-sizing:border-box;margin:0;padding:0}
html,body{width:949px;height:1200px;overflow:hidden;background:var(--backdrop)}
body{position:relative;font-family:"Questrial",sans-serif;color:var(--ink)}
.page{position:absolute;width:427px;height:550px;background:var(--paper);overflow:hidden}
.page--consent{left:40px;top:40px}
.page--risks{left:479px;top:40px}
.page--payment{left:40px;top:604px;height:549px}
.page--retainer{left:479px;top:604px;height:549px}
.abs{position:absolute}
.side-band{position:absolute;left:0;top:0;width:28px;height:100%;background:var(--band);border-bottom-right-radius:22px}
.side-band--short{width:32px;height:179px;border-bottom-right-radius:32px}
.corner-block{position:absolute;right:0;top:0;width:50px;height:207px;background:var(--band);border-bottom-left-radius:34px}
.brand{position:absolute;display:flex;align-items:center;gap:5px;font-family:"Montserrat",sans-serif;font-weight:600;color:var(--band)}
.brand__dot{border-radius:50%;background:var(--band)}
.doc-title{font-family:"Montserrat",sans-serif;font-weight:700;color:var(--navy);font-size:14.2px;line-height:17px}
.photo{position:absolute;left:190px;top:0;width:186px;height:101px;background:linear-gradient(120deg,#e4e8e4 0%,#cfd8d2 45%,#b9c0bf 100%)}
.form-line{position:absolute;font-size:5.7px;line-height:7px;white-space:nowrap}
.dots{display:inline-block;border-bottom:0.6px dotted #555;vertical-align:baseline}
.section-head{position:absolute;left:34px;font-family:"Montserrat",sans-serif;font-weight:600;color:var(--navy);font-size:8px;line-height:9px}
.body-text{position:absolute;font-size:5.8px;line-height:7.6px;text-align:justify}
.risk{position:absolute;left:37px;width:351px}
.risk--p1{left:34px;width:353px}
.risk__title{font-family:"Montserrat",sans-serif;font-weight:600;font-size:5.4px;line-height:7px}
.risk__text{font-size:5.6px;line-height:6.9px;text-align:justify;margin-top:3.5px}
.num{position:absolute;width:11px;height:11px;border-radius:50%;background:var(--paper);font-family:"Montserrat",sans-serif;font-weight:600;font-size:5.2px;line-height:11px;text-align:center}
.page-head{position:absolute;font-family:"Montserrat",sans-serif;font-weight:700;color:var(--navy);font-size:8.2px;padding-bottom:2px;border-bottom:0.8px solid var(--navy);white-space:nowrap}
.pay{position:absolute;left:54px;width:317px;font-size:6.3px;line-height:7.7px;text-align:justify}
.pay--label{font-family:"Montserrat",sans-serif;font-weight:600;font-size:6px}
.pay--under{text-decoration:underline;text-underline-offset:1.5px}
.pay em{font-style:italic}
.policy{position:absolute;left:64px;width:307px;display:flex;gap:6px;font-size:6.1px;line-height:7.6px;text-align:justify}
.policy svg{flex:0 0 12px;width:12px;height:11px;margin-top:-1px}
.footer-band{position:absolute;left:0;bottom:0;width:425px;height:104px;background:var(--footer)}
.footer-head{position:absolute;left:34px;top:10px;font-family:"Montserrat",sans-serif;font-weight:700;color:var(--navy);font-size:6.6px;border-bottom:0.7px solid var(--navy);padding-bottom:1px}
.doctor{position:absolute;left:34px;font-size:5px;line-height:7.5px}
.doctor b{font-family:"Montserrat",sans-serif;font-weight:600}
.doctor i{font-style:italic}
.office{position:absolute;left:205px;font-size:4.9px;line-height:6.8px;white-space:nowrap}
.office b{font-family:"Montserrat",sans-serif;font-weight:700}
</style>
</head>
<body>

<!-- Consent page -->
<section class="page page--consent">
  <div class="side-band"></div>
  <div class="corner-block"></div>
  <div class="brand" style="left:40px;top:24px;font-size:9px"><span class="brand__dot" style="width:9px;height:9px"></span>KVE</div>
  <h1 class="doc-title abs" style="left:34px;top:61px">PATIENT CONSENT<br>TO TREATMENT</h1>
  <div class="photo" role="img" aria-label="Photo of a patient in consultation with an orthodontist in a bright clinic"></div>

  <div class="form-line" style="left:34px;top:109px">I hereby authorize<span class="dots" style="width:284px"></span></div>
  <div class="form-line" style="left:35px;top:120px">To carry out orthodontic treatment and any other related procedures deemed necessary including X-rays, for</div>
  <div class="form-line" style="left:34px;top:130px">the welfare and treatment of:</div>
  <div class="form-line" style="left:34px;top:140px"><span class="dots" style="width:337px"></span></div>
  <div class="form-line" style="left:34px;top:153px">Signature of patient or parent/guardian:<span class="dots" style="width:68px"></span></div>
  <div class="form-line" style="left:34px;top:167px">Name<span class="dots" style="width:78px"></span></div>
  <div class="form-line" style="left:209px;top:167px">Relationship to patient<span class="dots" style="width:88px"></span></div>
  <div class="form-line" style="left:34px;top:188px">Date<span class="dots" style="width:9px"></span>/<span class="dots" style="width:9px"></span>/<span class="dots" style="width:16px"></span></div>
  <div class="form-line" style="left:209px;top:188px">Signature of Orthodontist<span class="dots" style="width:60px"></span></div>

  <h2 class="section-head" style="top:214px">ORTHODONTIC TREATMENT</h2>
  <p class="body-text" style="left:34px;top:224px;width:353px">Orthodontic treatment promotes a healthy smile, healthier teeth and gums and a better bite for normal chewing. Orthodontic treatment depends for much of its success on the understanding and co-operation of the patient. This form covers the usual material risks associated with Orthodontic treatment. You may ask your orthodontist to explain anything you do not understand. While recognizing he benefits of healthy teeth and a pleasing smile, you should also be aware that orthodontic treatment has limitations and potential risks and there may be alternative treatment options. You should clarify what is expected of you as a patient, or as the parent of a young patient, to achieve excellent results. Keep in mind that with orthodontic treatment, like other healing arts, results cannot be guaranteed. The unknown factor in any orthodontic correction is the response of the patient to the orthodontic treatment. Should you have any questions please ask.</p>

  <h2 class="section-head" style="top:303px">BENEFITS</h2>
  <p class="body-text" style="left:34px;top:313px;width:353px">Orthodontics plays an important role in improving overall oral health and achieving balance and harmony between the face and teeth for a beautiful, healthy smile, which may enhance one’s self esteem.The correct bite of teeth with health muscles and jaw joints will provide optimal chewing function . Properly aligned teeth are easier to brush and so the tendancy to decay may be decreased, as may the likelihood of developing disease of the gums and supporting bone Correctly aligned teeth are less likely to experience abnormal wear. Because of the individual conditions present and the limitations of treatment imposed by the nature each specific benefit may not be attainable for every patient.</p>

  <h2 class="section-head" style="top:378px">RISKS</h2>
  <p class="body-text" style="left:34px;top:388px;width:353px">All forms of medical and dental treatment including orthodontics, have some risk and limitations. Fortunately in orthodontics complications are infrequent and when they do occur they are usually of only minor consequence. Nevertheless, they should be considered when making the decision to undergo orthodontic treatment. The principal risks in orthodontic treatment pertain to:</p>

  <span class="num" style="left:22px;top:422px">1</span>
  <div class="risk risk--p1" style="top:424px">
    <h3 class="risk__title">Oral Hygiene</h3>
    <p class="risk__text">Orthodontic appliances do not cause tooth decay. Gum disease, tooth decay and permanent markings (decalcification) on teeth can occur if orthodontic patients eat food containing excessive sugar or do not brush teeth frequently or properly. These same problems can occur without orthodontic treatment but the risk is greater to an individual wearing braces. It is imperative during orthodontic treatment that extra care be taken with oral hygiene and tooth brushing in particular.</p>
  </div>
  <span class="num" style="left:22px;top:464px">2</span>
  <div class="risk risk--p1" style="top:466px">
    <h3 class="risk__title">Relapse</h3>
    <p class="risk__text">Teeth may have a tendency to change their positions after treatment. The long term faithful wearing of retainers should reduce this tendency. Teeth can however, move at any time, whether or not they have had orthodontic treatment. This is especially true during the late teen period when active growth of the facial bones is coming to an end. The most vulnerable teeth are those at the front. Throughout life, the bite can change adversely from various causes such as: eruption of wisdom teeth, growth or maturational changes, mouth breathing, playing of musical instruments and other oral habits. Very occasionally tooth movement will be severe enough to merit a further short course of treatment to ensure a satisfactory result.</p>
  </div>
</section>

<!-- Risks continued -->
<section class="page page--risks">
  <div class="side-band"></div>

  <span class="num" style="left:20px;top:35px">3</span>
  <div class="risk" style="top:37px">
    <h3 class="risk__title">Periodontal Health</h3>
    <p class="risk__text">The health of the bone and gums which support the teeth may be affected by orthodontic tooth movement if a condition already exists, and in some rare cases where a condition does not appear to exist. In general, orthodontic treatment lessens the possibility of tooth loss or gums infection due to misalignment of the teeth or jaws. Inflammation of the gums and loss of supporting bone can occur if bacterial plaque is not removed daily with good oral hygiene.</p>
  </div>
  <span class="num" style="left:20px;top:77px">4</span>
  <div class="risk" style="top:79px">
    <h3 class="risk__title">Root Shortening</h3>
    <p class="risk__text">In some patients the length of the roots of the teeth may be shortened during orthodontic treatment. Some patients are prone to this happening, some are not. It is nearly impossible to predict susceptibility. Usually this shortening does not have significant consequences, but on very rare occasions it may become a threat to the longevity of the teeth involved.</p>
  </div>
  <span class="num" style="left:20px;top:122px">5</span>
  <div class="risk" style="top:124px">
    <h3 class="risk__title">Jaw Joints</h3>
    <p class="risk__text">Occasionally patients may suffer pain or dysfunction in the jaw joints (T.M.J’s). This may present as joint pain, headaches or ear problems. These problems may occur with or without orthodontic treatment. Any of the above noted symptoms should be reported to the orthodontist. Some patients are susceptible to T.M.J. problems and some are not. Numerous studies have shown that movement of the teeth during orthodontic treatment is unrelated to the onset of T.M.J problems. Just as for painful conditions in other joints discomfort in T.M.J’s can last from a few days to several weeks or longer.</p>
  </div>
  <span class="num" style="left:20px;top:171px">6</span>
  <div class="risk" style="top:173px">
    <h3 class="risk__title">Tooth Vitality</h3>
    <p class="risk__text">Sometimes a tooth may have been traumatized by a previous accident or a tooth may be decayed or have large fillings which can cause damage to the nerve of the tooth. Orthodontic tooth movement in some cases aggravates this condition and in rare instances may lead to loss of tooth vitality and discolouration of the tooth requiring root canal treatment and other dental treatment to restore the colour of the tooth.</p>
  </div>
  <span class="num" style="left:20px;top:212px">7</span>
  <div class="risk" style="top:214px">
    <h3 class="risk__title">Loose appliances and discomfort</h3>
    <p class="risk__text">The gums, cheeks or lips may be scratched or irritated by newly placed appliances or by loose or broken appliances or by blows to the mouth. You will be given instruction or minimising these effects. Very rarely loose orthodontic appliances may be accidentally swallowed or aspirated. You should inform your orthodontist of any unusual symptoms, broken or loose appliances, as soon as they are noted. Usual post adjustment tenderness should be expected, and the period of tenderness or sensitivity varies with each patient and the procedure performed. (typical post adjustment tenderness may last 24 to 48 hours.)</p>
  </div>
  <span class="num" style="left:20px;top:268px">8</span>
  <div class="risk" style="top:270px">
    <h3 class="risk__title">Atypical Growth</h3>
    <p class="risk__text">Insufficient, excessive or asymmetrical changes in the growth of the jaws may limit our ability to achieve the desired result. If growth becomes disproportionate during orthodontic management the treatment may be prolonged. Growth changes that occur after orthodontic treatment may alter the quality of treatment results and may require further orthodontic treatment. In some cases of atypical growth, the bite may change so much that oral surgery is required to achieve the best possible result.</p>
  </div>
  <span class="num" style="left:20px;top:317px">9</span>
  <div class="risk" style="top:319px">
    <h3 class="risk__title">Headgear</h3>
    <p class="risk__text">If improperly handled, headgear may cause injury to the face. Patients are warned not to wear the appliance during the times of boisterous or competitive activity.</p>
  </div>
  <span class="num" style="left:20px;top:345px">10</span>
  <div class="risk" style="top:347px">
    <h3 class="risk__title">Treatment Time</h3>
    <p class="risk__text">The total time required to complete treatment may exceed the estimate. Poor co-operation in wearing the appliance or elastics the required hours per day, poor oral hygiene, broken appliances and missed appointments can lengthen the treatment time and affect the quality of the results.</p>
  </div>
  <span class="num" style="left:20px;top:379px">11</span>
  <div class="risk" style="top:381px">
    <h3 class="risk__title">Co-operation</h3>
    <p class="risk__text">Co-operation throughout treatment is your best guarantee of achieving a pleasing smile and good bite. Failure to co-operate could force the orthodontist to change the procedures and goals of your treatment. As a last resort treatment might have to be suspended. The consequences of early suspension may be worse than no treatment at all.</p>
  </div>
  <span class="num" style="left:20px;top:414px">12</span>
  <div class="risk" style="top:416px">
    <h3 class="risk__title">Ceramic Brackets</h3>
    <p class="risk__text">Where ceramic brackets have been used, there have been some reported incidents of patients experiencing bracket breakage or damage to teeth, including the wearing down of tooth enamel and flaking or fracturing of the tooth’s enamel on debanding. Fractured brackets may result in remnants which may be harmful to the patient especially if they are chewed on, swallowed or aspirated.</p>
  </div>
  <span class="num" style="left:20px;top:456px">13</span>
  <div class="risk" style="top:458px">
    <h3 class="risk__title">Complementary aesthetic dentistry</h3>
    <p class="risk__text">If your teeth vary from normal in the number, size or shape of the teeth, achievement of the ideal result (for example, complete closure of excessive space) may require restorative treatment. The most common types of complementary treatment are cosmetic bonding, crown and bridge restorative dental care and periodontal therapy.</p>
  </div>
  <span class="num" style="left:20px;top:490px">14</span>
  <div class="risk" style="top:492px">
    <h3 class="risk__title">General Health</h3>
    <p class="risk__text">General medical problems can affect orthodontic treatment. You should keep your orthodontist informed of any changes to you medical health.</p>
  </div>
</section>

<!-- Payment options -->
<section class="page page--payment">
  <div class="side-band side-band--short"></div>
  <div class="brand" style="left:52px;top:30px;font-size:12px"><span class="brand__dot" style="width:12px;height:12px"></span>KVE</div>
  <h2 class="page-head" style="left:249px;top:61px">PAYMENT OPTION SELECTION</h2>

  <p class="pay pay--label" style="top:112px">Patient Name: <span style="font-family:Questrial,sans-serif;font-weight:400">________________________________________________________________________</span></p>
  <p class="pay" style="top:136px"><em>Thank you for choosing Linden Orthodontics.</em></p>
  <p class="pay" style="top:148px">To assist with managing your treatment fees, please select your preferred payment method below. If you would prefer to pay at each scheduled appointment, please advise our reception team. Please note that appointments are generally scheduled every 6–8 weeks.</p>
  <p class="pay pay--label pay--under" style="top:184px">PLEASE SELECT ONE OPTION:</p>
  <p class="pay pay--label" style="top:205px">Credit Card Direct Debit</p>
  <p class="pay" style="top:217px">I would like to pay via credit card direct debit.</p>
  <p class="pay" style="top:229px">I understand that Linden Orthodontics will send me a secure PayLink payment link to enter my credit card details. The card provided will be securely stored and used as my nominated payment method for future scheduled payments relating to my treatment plan.</p>
  <p class="pay pay--label" style="top:266px">Monthly Direct Bank Transfer</p>
  <p class="pay" style="top:278px">I would like to pay via monthly direct bank transfer.</p>
  <p class="pay" style="top:290px">I understand that I am responsible for ensuring monthly payments are made on time in accordance with my agreed payment arrangement.</p>
  <p class="pay pay--label pay--under" style="top:320px">IMPORTANT</p>
  <p class="pay" style="top:332px">When making direct transfer payments, please use the patient's full name as the payment reference (for example: Jane Doe), rather than the account holder's name. This ensures payments are correctly allocated to your treatment account.</p>
  <p class="pay pay--label pay--under" style="top:370px">PATIENT DECLARATION</p>
  <p class="pay" style="top:382px">I have read and understood the payment options above and agree to my selected payment method.</p>
  <p class="pay" style="top:405px">Signature: ______________________________</p>
  <p class="pay" style="top:429px">Date: ________________________</p>
  <p class="pay pay--label pay--under" style="top:451px">OUR BANK ACCOUNT DETAILS:</p>
  <p class="pay" style="top:471px;line-height:7.6px"><b class="pay--label">Account Name:</b> Linden Orthodontics<br><b class="pay--label">Bank:</b> Harbour Bank<br><b class="pay--label">BSB:</b> 000 111<br><b class="pay--label">Account Number:</b> 4402187</p>
</section>

<!-- Retainer policy -->
<section class="page page--retainer">
  <div class="side-band side-band--short"></div>
  <div class="brand" style="left:52px;top:30px;font-size:12px"><span class="brand__dot" style="width:12px;height:12px"></span>KVE</div>
  <h2 class="page-head" style="left:277px;top:61px">OUR RETAINER POLICY</h2>

  <div class="policy" style="top:118px"><svg viewBox="0 0 12 11" aria-hidden="true"><path d="M1 6l3.5 3.5L11 1.5" fill="none" stroke="var(--tick)" stroke-width="2"/></svg><p>Wearing your retainers is the most important part of your orthodontic journey.</p></div>
  <div class="policy" style="top:133px"><svg viewBox="0 0 12 11" aria-hidden="true"><path d="M1 6l3.5 3.5L11 1.5" fill="none" stroke="var(--tick)" stroke-width="2"/></svg><p>Teeth shifting is a part of the natural ageing process just like getting wrinkles, so lifetime maintenance is crucial.</p></div>
  <div class="policy" style="top:156px"><svg viewBox="0 0 12 11" aria-hidden="true"><path d="M1 6l3.5 3.5L11 1.5" fill="none" stroke="var(--tick)" stroke-width="2"/></svg><p>Healthy teeth are not meant to be glued together, they are individual units and function independently. This is normally only done for areas of weak bone and gum or damaged teeth.</p></div>
  <div class="policy" style="top:179px"><svg viewBox="0 0 12 11" aria-hidden="true"><path d="M1 6l3.5 3.5L11 1.5" fill="none" stroke="var(--tick)" stroke-width="2"/></svg><p>For this reason WE DO NOT ENCOURAGE THE USE OF ‘BONDED’ OR ‘PERMANENT’ RETAINERS.</p></div>
  <div class="policy" style="top:194px"><svg viewBox="0 0 12 11" aria-hidden="true"><path d="M1 6l3.5 3.5L11 1.5" fill="none" stroke="var(--tick)" stroke-width="2"/></svg><p>Instead we advocate responsible use of removable retainers to maintain your smile.</p></div>
  <div class="policy" style="top:209px"><svg viewBox="0 0 12 11" aria-hidden="true"><path d="M1 6l3.5 3.5L11 1.5" fill="none" stroke="var(--tick)" stroke-width="2"/></svg><p>Permanent or bonded retainers are not actually permanent and can cause other unexpected problems after treatment is completed, such as difficulty to clean around those teeth which can cause plaque trapping and lead to localised gum and bone loss.</p></div>
  <div class="policy" style="top:240px"><svg viewBox="0 0 12 11" aria-hidden="true"><path d="M1 6l3.5 3.5L11 1.5" fill="none" stroke="var(--tick)" stroke-width="2"/></svg><p>They are subject to breaking frequently, which is the reason that when bonded retainers are placed, it is recommended that you still wear a removable retainer over them anyway.</p></div>
  <div class="policy" style="top:263px"><svg viewBox="0 0 12 11" aria-hidden="true"><path d="M1 6l3.5 3.5L11 1.5" fill="none" stroke="var(--tick)" stroke-width="2"/></svg><p>Bonded retainers only hold the front few teeth, whereas your orthodontic treatment involved improvements of ALL your teeth. Thus, holding the front teeth only gives the back teeth a chance to move out of alignment.</p></div>
  <div class="policy" style="top:293px"><svg viewBox="0 0 12 11" aria-hidden="true"><path d="M1 6l3.5 3.5L11 1.5" fill="none" stroke="var(--tick)" stroke-width="2"/></svg><p>The retainers we provide at Linden Orthodontics, are only worn at night and will hold ALL your teeth where they are at the end of your orthodontic treatment.</p></div>
  <div class="policy" style="top:316px"><svg viewBox="0 0 12 11" aria-hidden="true"><path d="M1 6l3.5 3.5L11 1.5" fill="none" stroke="var(--tick)" stroke-width="2"/></svg><p>Even excellent retainer wear will not guarantee that the teeth will stay exactly the same forever, due to the natural ageing and bone changing processes.</p></div>
  <div class="policy" style="top:339px"><svg viewBox="0 0 12 11" aria-hidden="true"><path d="M1 6l3.5 3.5L11 1.5" fill="none" stroke="var(--tick)" stroke-width="2"/></svg><p>Minor alignment adjustments may be made to your retainers in the future to ensure that you remain happy with your smile.</p></div>
  <div class="policy" style="top:362px"><svg viewBox="0 0 12 11" aria-hidden="true"><path d="M1 6l3.5 3.5L11 1.5" fill="none" stroke="var(--tick)" stroke-width="2"/></svg><p>After 2 years of retainer reviews, further follow up care may be charged at the current office visit rate.</p></div>
  <div class="policy" style="top:385px"><svg viewBox="0 0 12 11" aria-hidden="true"><path d="M1 6l3.5 3.5L11 1.5" fill="none" stroke="var(--tick)" stroke-width="2"/></svg><p>Lost or broken retainers will incur a fee for replacement or repair.</p></div>

  <footer class="footer-band">
    <h3 class="footer-head">REGISTERED SPECIALIST ORTHODONTISTS</h3>
    <p class="doctor" style="top:22px"><b>Dr Owen Hale</b><br><i>DCD, MOrth, MRACDS (Orth), BDSc (Hons)</i></p>
    <p class="doctor" style="top:44px"><b>Dr Clara Renwick</b><br><i>MDSc, Grad Dip Clin Dent, BDSc(Hons)</i></p>
    <p class="doctor" style="top:66px"><b>Dr Sam Petrov</b><br><i>MDSc, Grad Dip Clin Dent, MOrth, BDSc</i></p>
    <p class="office" style="top:22px">14 Elm Road, Northgate VIC 3001<br><b>T.</b> 03 9000 1101 <b>F.</b> 03 9000 1102 <b>E.</b> northgate@linden-ortho.example</p>
    <p class="office" style="top:43px">52 Ridge Lane, Eastvale VIC 3102 (Cnr Park Street)<br><b>T.</b> 03 9000 2201 <b>F.</b> 03 9000 2202 <b>E.</b> eastvale@linden-ortho.example</p>
    <p class="office" style="top:64px">9 Mill Street Hillside Vic 3160<br><b>T.</b> 03 9000 3301 <b>F.</b> 03 9000 3302 <b>E.</b> hillside@linden-ortho.example</p>
  </footer>
</section>

</body>
</html>
```